Honey Bottle Labels for Honey Business

The honey is a niche product and the logo should exude a strong impression of wild and raw honey and natural – as in natural beekeeping. We try to keep things as simple as possible; this includes the processes the honey goes through.
We are looking for something with a gourmet / classy upmarket look and feel design. For example: Ideas with bees, honeycomb, modern or hexagonal feature; something eye catching, but not too busy.
Our honey is all natural and organic. We are a clean, simple yet sophisticated business, so would like our logo to reflect these principles.

Feel free to expand your creativity to anything you may think would look awesome and original!

The label needs to contain:
1. Our company logo. (Please see attached)
2. 100% Pure Raw Honey / Local
3. Net Wt: 16 oz (454 g) (this is the weight of the honey and will need to be modified based on bottle size.)
4. Address, Pine Hollow, MN 55990 (not larger than 1/16th inch)

Needs to be versatile to include possibility of clear label, I have included some example pictures as ideas (oval, round, square tags)

Sizes needed:
Large oval 2 5/8" x 4 1/2"
Small oval: 1 3/4" wide x 3" tall
Rectangle 1 3/4" tall x 5" wide
Round diameter 2.5"

Target Market(s)

Gourmet stores, market stall, local tourist market, potential store door sales

Requirements
Must have
• - A design that can be used on various packaging, jars and containers. We are hoping to scale up the production and want something to suit.
• - has to have a wow to stand out on the supermarket shelves
Nice to have
• Things we like:
• Minimalist designs
• Clever designs
• We don't like hand drawn font types
• We are open to the use of a hexagon in the logo, but not must have
Should not have
• Things we do not like:
• Too many colors

```html
<!DOCTYPE html>
<html lang="en">
<head>
<meta charset="utf-8">
<title>Amberfield Honey – Oval Bottle Label</title>
<link href="https://fonts.googleapis.com/css2?family=Lato:wght@400;700;900&family=Oswald:wght@700&display=swap" rel="stylesheet">
<style>
  :root {
    --honey-orange: #f29a1f;
    --honey-light: #fbd79e;
    --honey-pale: #fdeed6;
    --label-white: #ffffff;
    --ink: #1f1f1f;
    --dash-grey: #555555;
    --band-grey: #b9b9b9;
    --page-bg: #f1efec;
  }
  * { margin: 0; padding: 0; box-sizing: border-box; }
  html, body {
    width: 1200px; height: 900px; overflow: hidden;
    background: var(--page-bg);
    font-family: "Lato", Arial, sans-serif;
  }
  .canvas { position: relative; width: 1200px; height: 900px; }

  .oval-label {
    position: absolute; left: 365px; top: 45px;
    width: 470px; height: 810px;
    border-radius: 50% / 50%;
    overflow: hidden;
    background: var(--label-white);
    box-shadow: 0 4px 18px rgba(0,0,0,.12);
  }
  .honeycomb-field {
    position: absolute; left: 0; top: 150px; width: 100%; height: 300px;
    background: linear-gradient(180deg, var(--honey-light) 0%, var(--honey-pale) 55%, var(--label-white) 100%);
  }
  .top-cap {
    position: absolute; left: 0; top: 0; width: 100%; height: 190px;
    background: var(--honey-orange);
  }
  .logo-disc {
    position: absolute; left: 75px; top: 30px;
    width: 320px; height: 320px; border-radius: 50%;
    background: var(--honey-orange);
    display: flex; align-items: center; justify-content: center;
  }
  .logo-ring {
    width: 272px; height: 272px; border-radius: 50%;
    border: 3px solid var(--label-white);
    display: flex; flex-direction: column; align-items: center; justify-content: center;
    gap: 14px;
  }
  .logo-dot { width: 22px; height: 22px; border-radius: 50%; background: var(--label-white); }
  .brand-name {
    color: var(--label-white); font-weight: 400; font-size: 36px;
    line-height: 1.05; text-align: center;
  }

  .claim-block {
    position: absolute; left: 0; top: 455px; width: 100%;
    text-align: center; color: var(--honey-orange);
  }
  .dash-rule {
    width: 250px; margin: 0 auto; border-top: 2px dashed var(--dash-grey);
  }
  .claim-line {
    font-weight: 700; font-size: 34px; margin-top: 10px; letter-spacing: .5px;
  }
  .product-name {
    font-family: "Oswald", "Arial Narrow", sans-serif;
    font-weight: 700; font-size: 92px; line-height: 1; letter-spacing: 1px;
    margin-top: -2px;
  }
  .origin-line {
    display: flex; align-items: center; justify-content: center; gap: 12px;
    font-weight: 700; font-size: 26px; margin-top: 2px;
  }
  .origin-line .dash { width: 80px; border-top: 2px dashed var(--dash-grey); }

  .net-weight {
    position: absolute; left: 0; top: 720px; width: 100%;
    text-align: center; color: var(--ink); font-size: 24px; line-height: 1.3;
  }

  .address-band {
    position: absolute; left: 0; bottom: 0; width: 100%; height: 68px;
  }
  .address-band svg { position: absolute; left: 0; top: 0; }
  .address-text {
    position: absolute; left: 0; top: 24px; width: 100%;
    text-align: center; color: var(--label-white);
    font-weight: 700; font-size: 11px; line-height: 1.35;
  }
</style>
</head>
<body>
<main class="canvas">
  <section class="oval-label" aria-label="Oval honey bottle label">
    <div class="honeycomb-field" role="img" aria-label="Soft honeycomb hexagon pattern fading from light orange to white"></div>
    <div class="top-cap"></div>
    <div class="logo-disc">
      <div class="logo-ring">
        <span class="logo-dot"></span>
        <span class="brand-name">amberfield<br>honey</span>
      </div>
    </div>

    <div class="claim-block">
      <div class="dash-rule"></div>
      <p class="claim-line">100% PURE RAW</p>
      <h1 class="product-name">HONEY</h1>
      <p class="origin-line"><span class="dash"></span>LOCAL<span class="dash"></span></p>
    </div>

    <p class="net-weight">Net Wt: 16 oz<br>(454 g)</p>

    <div class="address-band">
      <svg width="470" height="68" viewBox="0 0 470 68" aria-hidden="true">
        <path d="M0 14 Q235 -6 470 14 L470 68 L0 68 Z" fill="var(--band-grey)"/>
        <path d="M0 20 Q235 0 470 20 L470 68 L0 68 Z" fill="var(--honey-orange)"/>
      </svg>
      <p class="address-text">Pine Hollow, MN 55990<br>+00 000 0000</p>
    </div>
  </section>
</main>
</body>
</html>
```